Tidal Quill is a premium Spa and Salon only professional tanning brand.

We need a email template/newsletter that we can send to our client base any time we would like to share information with them.
Whether this is launching our Christmas gift, or sharing up and coming training dates it will be another avenue for us to stay in touch with our clients.
We like to think ourselves as the 'Verrington handbag' in the tanning world, Tidal Quill is a brand that is desirable and exclusive and has people hooked once they trial the brand and are blown away by the results.
www.tidal-quill-example.com

```html
<!DOCTYPE html>
<html lang="en">
<head>
<meta charset="utf-8">
<title>Tidal Quill Newsletter</title>
<link rel="stylesheet" href="https://fonts.googleapis.com/css2?family=Jost:wght@400;500&display=swap">
<style>
  :root {
    --copper: #a5623c;
    --sand: #dcb896;
    --rule: #d9c4ae;
    --grey: #808080;
    --paper: #ffffff;
    --badge: #c9a58c;
  }
  * { margin: 0; padding: 0; box-sizing: border-box; }
  html, body { width: 896px; height: 1200px; overflow: hidden; background: var(--paper); }
  body { font-family: "Jost", sans-serif; color: var(--grey); }
  .newsletter { position: relative; width: 896px; height: 1200px; overflow: hidden; }
  .top-band {
    position: absolute; left: 0; top: 0; width: 896px; height: 8px;
    background: linear-gradient(90deg, #d8b898 0%, #a86a45 50%, #d8b898 100%);
  }
  .brand {
    position: absolute; left: 39px; top: 52px;
    display: flex; align-items: center; gap: 14px;
    font-size: 52px; font-weight: 500; line-height: 1; color: var(--copper);
    letter-spacing: 1px;
  }
  .brand-dot { width: 22px; height: 22px; border-radius: 50%; background: var(--copper); }
  .social-button {
    position: absolute; left: 622px; top: 95px; width: 246px; height: 47px;
    background: var(--copper); color: var(--paper);
    display: flex; align-items: center; justify-content: center; gap: 10px;
    font-size: 20px; font-weight: 500; text-decoration: none;
  }
  .social-square { width: 14px; height: 14px; background: var(--paper); }
  .rule { position: absolute; left: 0; width: 896px; height: 1px; background: var(--rule); }
  .rule-top { top: 162px; }
  .rule-bottom { top: 233px; }
  .section-title {
    position: absolute; left: 0; top: 174px; width: 896px; text-align: center;
    font-size: 34px; font-weight: 400; color: var(--copper); letter-spacing: 0.5px;
  }
  .product-shot {
    position: absolute; left: 134px; top: 274px; width: 303px; height: 381px;
    border-radius: 10px;
    background: linear-gradient(180deg, #f6f4f2 0%, #ece6e1 55%, #d7bfa8 80%, #f3efeb 100%);
  }
  .intro {
    position: absolute; left: 540px; top: 298px; width: 320px;
    font-size: 20px; line-height: 26px; color: var(--grey);
    hyphens: auto; -webkit-hyphens: auto;
  }
  .intro p + p { margin-top: 26px; }
  .button {
    position: absolute; display: flex; align-items: center; justify-content: center;
    background: var(--sand); color: var(--paper); text-decoration: none; font-weight: 400;
  }
  .button-try { left: 541px; top: 622px; width: 202px; height: 46px; font-size: 26px; }
  .headline {
    position: absolute; left: 20px; top: 740px; width: 486px; text-align: center;
    font-size: 37px; line-height: 44px; font-weight: 500; color: var(--copper);
  }
  .divider {
    position: absolute; left: 143px; top: 916px; width: 255px;
    border-top: 1px dashed var(--copper);
  }
  .stockist-lead {
    position: absolute; left: 20px; top: 996px; width: 498px; text-align: center;
    font-size: 24px; color: var(--grey);
  }
  .button-stockist { left: 116px; top: 1057px; width: 304px; height: 76px; font-size: 36px; }
  .leaf-flourish {
    position: absolute; left: 530px; top: 680px; width: 366px; height: 520px;
    background: radial-gradient(ellipse 60% 55% at 55% 62%,
      rgba(184,105,63,0.38) 0%, rgba(226,204,196,0.45) 45%, rgba(255,255,255,0) 80%);
  }
  .badge { position: absolute; border-radius: 50%; background: var(--badge); }
  .badge-cruelty { left: 716px; top: 1108px; width: 56px; height: 56px; }
  .badge-organic { left: 808px; top: 1104px; width: 60px; height: 60px; }
</style>
</head>
<body>
<main class="newsletter">
  <div class="top-band"></div>

  <header>
    <div class="brand"><span class="brand-dot"></span>Tidal Quill</div>
    <a class="social-button" href="#"><span class="social-square"></span>Find us on Kinloop</a>
  </header>

  <div class="rule rule-top"></div>
  <h1 class="section-title">NEWSLETTER</h1>
  <div class="rule rule-bottom"></div>

  <div class="product-shot" role="img" aria-label="Three white tanning product bottles with leaf artwork and an organic seal"></div>

  <section class="intro">
    <p>Lorem ipsum dolor sit amet, consectetur adipiscing elit.</p>
    <p>Quisque sapien mi, tempus quis auctor in, congue sit amet nisl. Pellentesque porta dui non bibendum venenatis.</p>
    <p>Phasellus vitae tellus nisl. Nulla tincidunt porta urna sed laoreet. Integer amet.</p>
  </section>
  <a class="button button-try" href="#">Try it now!</a>

  <div class="leaf-flourish" role="img" aria-label="Decorative sweep of falling copper autumn leaves along a soft blush curve"></div>

  <h2 class="headline">Lorem ipsum dolor sit amet, consectetur adipiscing elit. Vestibulum turpis duis.</h2>
  <div class="divider"></div>
  <p class="stockist-lead">Lorem ipsum dolor sit amet, consectetur:</p>
  <a class="button button-stockist" href="#">Find a Stockist</a>

  <div class="badge badge-cruelty"></div>
  <div class="badge badge-organic"></div>
</main>
</body>
</html>
```